Tidewell Homes Website Redesign

We need a website redesign for an existing website www.tidewellhomes.com.au. A home page and a property page needs to be designed...have attached layout for property page which sits under House and Land.

Have also attached logo.

Site will be built on Pyx Frame Core 5x content management system so design needs to be PFC compatible and using system fonts as well eg Arial, Verdana or Tahoma.

Target Market(s)

Builders and owner builders

Industry/Entity Type

Construction

Number of Pages Required

2 pages

Requirements
Must have
• Site Map

• o Home
• o Inclusions
• o Designs
• o House and Land
• ? Gallery
• o Selection Centre
• o Redevelopment
• o Contact Us

• Design Brief

• o Likes www.ambrosecoastal.com.au as a corporate homepage layout...with buttons across the bottom etc
• o Likes http://www.valdrenhomes.com.au/
• o Likes http://www.corvask.com.au/, but this site is built entirely in flash so some functionality won’t be possible.
• • Logo and phone number across top 02 6378 9152
• • Rolling banner along bottom of page with gallery photos
• • Horizontal navigational bar
• • Content below the main menu
• • Large contact us button.
• - Need to ensure BTG and Guild Constructor logo is on every page (perhaps in footer???)
• - Need
• ACN 061 372 908 NSW License No. 483052K ACT License No. 3142
• also in footer of every page

• Colours are, maroon, gold and predominately white. I don"t have any problems with some elements of light grey.

```html
<!DOCTYPE html>
<html lang="en">
<head>
<meta charset="utf-8">
<title>Tidewell Homes – Home and Property Pages</title>
<link href="https://fonts.googleapis.com/css2?family=Arimo:wght@400;700&display=swap" rel="stylesheet">
<style>
:root{
  --maroon:#8a0f24;
  --maroon-dark:#5c0616;
  --maroon-deep:#4a0411;
  --gold:#c9a24a;
  --ink:#333;
  --muted:#555;
  --grey-light:#e6e6e6;
  --grey-mid:#b9b9b9;
  --grey-dark:#4a4a4a;
  --white:#fff;
}
*{box-sizing:border-box;margin:0;padding:0}
html,body{width:1200px;height:3416px;overflow:hidden;background:var(--white)}
body{position:relative;font-family:"Arimo",Arial,sans-serif;color:var(--ink)}
.abs{position:absolute}
.page-label{position:absolute;left:0;width:1200px;text-align:center;font-size:26px;color:#444;letter-spacing:.5px}

/* header band */
.header{position:absolute;left:2px;width:1196px;
  background:radial-gradient(ellipse at 50% 30%,#9c1a2e 0%,var(--maroon) 45%,var(--maroon-dark) 100%);
  border-bottom:3px solid var(--white);box-shadow:0 2px 0 #9c1a2e}
.header-shade{position:absolute;left:0;width:1200px;height:40px;background:linear-gradient(#d9d9d9,#fff)}
.logo-box{position:absolute;left:166px;width:196px;height:113px;background:linear-gradient(#fff,#ececec);
  border:1px solid #ccc;box-shadow:0 2px 4px rgba(0,0,0,.4);display:flex;align-items:center;justify-content:center;gap:8px}
.logo-box .mark{width:14px;height:14px;background:var(--maroon)}
.logo-box .name{font-size:22px;font-weight:700;color:var(--maroon)}
.call-now{position:absolute;right:150px;font-size:19px;font-weight:700;color:var(--white)}
.photo{position:absolute;border:3px solid var(--white);box-shadow:0 2px 6px rgba(0,0,0,.45)}
.photo.house{background:linear-gradient(#8fb6dc 0%,#c9d9e6 35%,#6d6a66 55%,#d8cfa8 70%,#5d8a3a 100%)}
.photo.kitchen{background:linear-gradient(90deg,#d9d9d6,#f2f2f0 60%,#a9a9a4)}
.photo.villa{background:linear-gradient(#9cc0e2,#e8d9a6 45%,#c06a3a 75%,#6b8b3d)}
.tagline{position:absolute;left:0;width:1196px;text-align:center;color:var(--white);text-transform:uppercase}

/* navigation */
.nav{position:absolute;left:166px;width:884px;height:38px;display:flex;
  background:linear-gradient(#f4f4f4,#d4d4d4);border-bottom:1px solid #bbb}
.nav a{flex:1;display:flex;align-items:center;justify-content:center;font-size:13px;font-weight:700;
  color:#333;text-decoration:none;border-right:1px solid #fff}
.nav a.active{background:linear-gradient(#5a5a5a,#2e2e2e);color:var(--white)}
.nav a.current{background:linear-gradient(#8a8a8a,#5c5c5c);color:var(--white)}

/* home content */
.welcome{position:absolute;left:166px;top:620px;font-size:20px;font-weight:400;color:var(--maroon)}
.copy{position:absolute;left:166px;font-size:10.5px;line-height:15px;color:var(--muted)}
.copy b{color:var(--maroon)}
.divider{position:absolute;left:758px;top:623px;height:504px;border-left:1px dotted #bbb}
.side-title{position:absolute;left:809px;top:626px;font-size:15px;color:var(--maroon)}
.gallery-big{position:absolute;left:809px;top:656px;width:213px;height:144px;border:2px solid var(--maroon);
  background:linear-gradient(#b7cde0,#d9c9a4 50%,#8a7c66 80%,#7b8a55)}
.thumb{position:absolute;width:104px;height:69px}
.t-bath{background:linear-gradient(135deg,#f3e6c9,#d8b77d)}
.t-stair{background:linear-gradient(135deg,#6e4a32,#c9a27a)}
.t-kit{background:linear-gradient(135deg,#e8e4da,#b8b1a2)}
.t-bed{background:linear-gradient(135deg,#d9cbb3,#8b7458)}
.t-lounge{background:linear-gradient(135deg,#9a8a76,#3a2e28)}
.t-family{background:linear-gradient(135deg,#6b4a3a,#a99480)}
.more{position:absolute;font-size:9px;font-weight:700;color:#444}
.contact-btn{position:absolute;left:823px;top:1066px;width:186px;height:70px;border-radius:8px;
  background:linear-gradient(#a3182f,var(--maroon-dark));box-shadow:0 3px 5px rgba(0,0,0,.45);
  display:flex;align-items:center;justify-content:center;color:var(--white);font-size:21px;font-weight:700;letter-spacing:.5px}
.award-cap{position:absolute;left:232px;width:431px;text-align:center;font-size:10.5px;font-weight:700;color:#555;line-height:13px}
.award-text{position:absolute;left:232px;top:1063px;width:431px;text-align:center;color:var(--white);font-size:14px;line-height:20px}

/* footer */
.footer{position:absolute;left:0;width:1200px;background:linear-gradient(var(--maroon-dark),var(--maroon) 60%,#7a0c20)}
.footer-base{position:absolute;left:0;width:1200px;background:var(--maroon-deep);color:var(--white);
  font-size:9px;font-weight:700;text-align:center;line-height:11px;padding-top:9px}
.links{position:absolute;color:var(--white)}
.links h4{font-size:16px;font-weight:700;margin-bottom:10px}
.links ul{list-style:none}
.links li{list-style:none;font-size:10px;font-weight:700;letter-spacing:.5px;height:20px}
.links li::before{content:"»";margin-right:5px}
.partners{position:absolute;left:830px;width:220px;height:113px;background:linear-gradient(#fff,#e2e2e2);border:1px solid #ccc}
.partners p{position:absolute;left:11px;top:9px;font-size:15px;color:var(--maroon)}
.badge-a{position:absolute;left:30px;top:38px;width:100px;height:52px;background:#1c2f6b;border-radius:4px}
.badge-b{position:absolute;left:153px;top:30px;width:54px;height:66px;background:#1f7a3a;border-radius:10px}

/* property page */
.price-box{position:absolute;left:455px;top:1863px;width:300px;height:40px;background:var(--maroon);
  color:var(--white);font-size:27px;display:flex;align-items:center;justify-content:center}
.section-bar{position:absolute;left:166px;top:1945px;width:884px;height:40px;background:linear-gradient(#7a7a7a,#545454);
  color:var(--white);font-size:19px;font-weight:700;padding-left:71px;display:flex;align-items:center}
.exterior{position:absolute;left:237px;top:2022px;width:609px;height:329px;border-radius:6px;
  box-shadow:0 2px 6px rgba(0,0,0,.4);background:linear-gradient(#dfe8f0 0%,#b5c6d6 25%,#77726d 45%,#a4a09a 65%,#8d9a6d 85%,#6f8a45)}
.feature-icon{position:absolute;left:892px;width:52px;height:50px;border-radius:8px;background:linear-gradient(#f7f7f7,#c9c9c9);
  box-shadow:0 1px 3px rgba(0,0,0,.4);display:flex;align-items:center;justify-content:center}
.feature-num{position:absolute;left:892px;width:52px;text-align:center;font-size:19px;color:#222}
.strip{position:absolute;left:228px;top:2389px;width:755px;height:179px;background:#d6d6d6}
.strip .thumb-l{position:absolute;top:22px;width:201px;height:132px;border:2px solid var(--white)}
.plan{position:absolute;left:236px;top:2627px;width:465px;height:294px;background:linear-gradient(#fbfbfb,#eef0f4);
  border:1px solid #ccc;box-shadow:0 1px 4px rgba(0,0,0,.3)}
.panel{position:absolute;background:#f0f0f0;border:1px solid #d2d2d2}
.panel-head{position:absolute;left:0;top:0;width:100%;background:linear-gradient(#9e152c,var(--maroon-dark));
  color:var(--white);font-size:19px;font-weight:700;display:flex;align-items:center;justify-content:center;border-radius:6px 6px 0 0}
.deal-img{position:absolute;left:24px;top:44px;width:195px;height:127px;border:1px solid #aaa;
  background:linear-gradient(#b7cde0,#d9c9a4 50%,#8a7c66 80%,#7b8a55)}
.deal-text{position:absolute;left:9px;top:188px;font-size:10px;line-height:15px;color:#666}
.msg-text{position:absolute;left:8px;top:58px;width:450px;font-size:10px;line-height:16.8px;color:#555}
.contact-info{position:absolute;left:735px;top:2949px;width:247px;height:167px;border-radius:6px;
  background:linear-gradient(#9a142b,var(--maroon-dark));box-shadow:0 2px 4px rgba(0,0,0,.4);color:var(--white);text-align:center}
.contact-info h3{font-size:18px;font-weight:700;margin-top:10px}
.contact-info p{font-size:14.5px;font-weight:700;line-height:20px}
</style>
</head>
<body>

<!-- ================= HOME PAGE ================= -->
<div class="page-label" style="top:52px">HOME PAGE</div>

<header class="header" style="top:110px;height:420px"></header>
<div class="logo-box" style="top:110px"><span class="mark"></span><span class="name">Tidewell Homes</span></div>
<div class="call-now" style="top:126px">Call Now: 02 6378 9152</div>

<svg class="abs" style="left:215px;top:360px" width="28" height="36" viewBox="0 0 28 36" aria-hidden="true"><path d="M22 3 L7 18 L22 33" fill="none" stroke="#fff" stroke-width="6"/></svg>
<div class="photo kitchen" role="img" aria-label="Modern kitchen interior" style="left:267px;top:289px;width:95px;height:178px"></div>
<div class="photo villa" role="img" aria-label="Arched entry of a rendered villa" style="left:840px;top:289px;width:96px;height:178px"></div>
<div class="photo house" role="img" aria-label="Two-storey stone-faced family home" style="left:359px;top:262px;width:486px;height:233px"></div>
<svg class="abs" style="left:962px;top:360px" width="28" height="36" viewBox="0 0 28 36" aria-hidden="true"><path d="M6 3 L21 18 L6 33" fill="none" stroke="#fff" stroke-width="6"/></svg>
<div class="tagline" style="top:500px;font-size:21px">We will build your home on budget and on time</div>
<div class="header-shade" style="top:533px"></div>

<nav class="nav" style="top:540px">
  <a class="active">Home</a><a class="current">Inclusions Designs</a><a>House and Land</a><a>Gallery</a><a>Selection Centre</a><a>Redevelopment</a><a>Contact Us</a>
</nav>

<h1 class="welcome">Welcome to Tidewell Homes Constructions.</h1>
<p class="copy" style="top:661px;width:320px"><b>Tidewell Homes Constructions</b> was established in February 2001 by Owen Carlisle and Lachlan Petrie. Between the two directors the company has over 40 years building experience in the ACT Region and both directors are individually licensed builders.</p>
<p class="copy" style="top:736px;width:320px">We offer a range of flexible and varied home designs, these designs can be built on your land or ours. We will also quote individual designs should one of our plans be unsuitable to your needs or should you desire a more customized home.</p>
<p class="copy" style="top:812px;width:540px">Tidewell Homes is a member of the Building Trades Guild and Guild Constructors Association. In addition both directors of the company are also accredited "Ecobuild Professionals".</p>
<p class="copy" style="top:857px;width:540px">Tidewell Homes uses only quality suppliers and our team of contractors are reliable, qualified and assist us to achieve a quality finish.</p>
<p class="copy" style="top:903px;width:540px">Both directors are hands on and personally oversee the construction process as well as being available to owners to attend to queries or concerns. Our aim is to build quality project homes whilst providing a boutique style service.</p>
<div class="abs" role="img" aria-label="Directors with a family outside a new home" style="left:541px;top:666px;width:160px;height:106px;border:1px solid var(--maroon);background:linear-gradient(90deg,#4a2c1e,#8a6a50 50%,#c9b49a)"></div>

<div class="award-cap" style="top:1023px">Award Winning Builders 02, 03 &amp; 05<br>Most Recently</div>
<svg class="abs" style="left:228px;top:1056px" width="440" height="84" viewBox="0 0 440 84" aria-hidden="true">
  <polygon points="4,2 436,2 426,42 436,82 4,82 14,42" fill="#b3203a"/>
  <polygon points="14,8 426,8 418,42 426,76 14,76 22,42" fill="#7d0b1f"/>
</svg>
<div class="award-text">Winner BTG 'ACT Energy Efficient Home of the Year' 2005<br>Finalist BTG 'ACT Display Home of the Year' 2005<br>Finalist BTG 'ACT House of the Year' 2005</div>

<div class="divider"></div>
<div class="side-title">Latest Gallery</div>
<div class="gallery-big" role="img" aria-label="Contemporary home with timber deck"></div>
<div class="thumb t-bath" role="img" aria-label="Corner spa bathroom" style="left:809px;top:809px"></div>
<div class="thumb t-stair" role="img" aria-label="Timber staircase" style="left:917px;top:809px"></div>
<div class="thumb t-kit" role="img" aria-label="Kitchen" style="left:809px;top:880px"></div>
<div class="thumb t-bed" role="img" aria-label="Main bedroom" style="left:917px;top:880px"></div>
<div class="thumb t-lounge" role="img" aria-label="Living room" style="left:809px;top:953px"></div>
<div class="thumb t-family" role="img" aria-label="Family in a new home" style="left:917px;top:953px"></div>
<div class="more" style="left:988px;top:1029px">More</div>
<div class="contact-btn">CONTACT US</div>

<footer class="footer" style="top:1173px;height:144px"></footer>
<div class="links" style="left:166px;top:1186px"><h4>Links 1</h4><ul><li>Navgation 1</li><li>Navgation 2</li><li>Navgation 3</li><li>Navgation 4</li></ul></div>
<div class="links" style="left:277px;top:1186px"><h4>Links 2</h4><ul><li>Navgation 1</li><li>Navgation 2</li><li>Navgation 3</li><li>Navgation 4</li></ul></div>
<div class="links" style="left:395px;top:1186px"><h4>Links 3</h4><ul><li>Navgation 1</li><li>Navgation 2</li><li>Navgation 3</li><li>Navgation 4</li></ul></div>
<div class="links" style="left:505px;top:1186px"><h4>Links 4</h4><ul><li>Navgation 1</li><li>Navgation 2</li><li>Navgation 3</li><li>Navgation 4</li></ul></div>
<div class="partners" style="top:1189px"><p>Our Parners</p><div class="badge-a"></div><div class="badge-b"></div></div>
<div class="footer-base" style="top:1317px;height:33px">© Tidewell Homes Constructions 2004 Owned and operated by Harrowfield ( Canberra ) Pty Limited<br>ACN 061 372 908 NSW License No. 483052K ACT License No. 3142</div>

<!-- ================= PROPERTY PAGE ================= -->
<div class="page-label" style="top:1447px">PROPERTY PAGE</div>

<header class="header" style="top:1518px;height:252px"></header>
<div class="logo-box" style="top:1518px"><span class="mark"></span><span class="name">Tidewell Homes</span></div>
<div class="call-now" style="top:1533px">Call Now: 02 6378 9152</div>
<div class="photo kitchen" role="img" aria-label="Modern kitchen interior" style="left:602px;top:1589px;width:64px;height:119px"></div>
<div class="photo villa" role="img" aria-label="Arched entry of a rendered villa" style="left:986px;top:1589px;width:64px;height:119px"></div>
<div class="photo house" role="img" aria-label="Two-storey stone-faced family home" style="left:663px;top:1571px;width:326px;height:155px"></div>
<div class="tagline" style="top:1741px;left:440px;width:770px;font-size:15.5px;text-align:center">We will build your home on budget and on time</div>
<div class="header-shade" style="top:1773px"></div>

<nav class="nav" style="top:1779px">
  <a class="active">Home</a><a class="current">Inclusions Designs</a><a>House and Land</a><a>Gallery</a><a>Selection Centre</a><a>Redevelopment</a><a>Contact Us</a>
</nav>

<div class="price-box">SUBURB $400,000</div>
<div class="section-bar">Exterior View</div>
<div class="exterior" role="img" aria-label="Single-storey brick home with double garage"></div>

<div class="feature-icon" style="top:2026px"><svg width="34" height="24" viewBox="0 0 34 24" aria-hidden="true"><path d="M3 2v20M31 10v12M3 16h28M3 10h28" fill="none" stroke="#333" stroke-width="3"/><rect x="6" y="4" width="8" height="5" fill="#333"/></svg></div>
<div class="feature-num" style="top:2084px">4</div>
<div class="feature-icon" style="top:2151px"><svg width="36" height="22" viewBox="0 0 36 22" aria-hidden="true"><path d="M2 8h32v4a8 8 0 0 1-8 8H10a8 8 0 0 1-8-8z" fill="#333"/><path d="M8 20l-2 2M28 20l2 2" stroke="#333" stroke-width="2"/></svg></div>
<div class="feature-num" style="top:2209px">6</div>
<div class="feature-icon" style="top:2275px"><svg width="34" height="30" viewBox="0 0 34 30" aria-hidden="true"><path d="M2 10L17 2l15 8" fill="none" stroke="#333" stroke-width="2.5"/><path d="M8 22l3-8h12l3 8z" fill="#333"/><rect x="6" y="21" width="22" height="5" rx="2" fill="#333"/></svg></div>
<div class="feature-num" style="top:2332px">2</div>

<div class="strip">
  <svg class="abs" style="left:10px;top:72px" width="30" height="36" viewBox="0 0 30 36" aria-hidden="true"><path d="M23 3L8 18l15 15" fill="none" stroke="#111" stroke-width="6"/></svg>
  <div class="thumb-l t-bed" role="img" aria-label="Bedroom" style="left:52px"></div>
  <div class="thumb-l t-bath" role="img" aria-label="Corner spa bathroom" style="left:277px"></div>
  <div class="thumb-l t-kit" role="img" aria-label="Kitchen" style="left:503px"></div>
  <svg class="abs" style="left:718px;top:72px" width="30" height="36" viewBox="0 0 30 36" aria-hidden="true"><path d="M7 3l15 15L7 33" fill="none" stroke="#111" stroke-width="6"/></svg>
</div>

<div class="plan" role="img" aria-label="Floor plan sheet for the home design with price and room dimensions"></div>

<section class="panel" style="left:735px;top:2627px;width:249px;height:294px">
  <div class="panel-head" style="height:34px">Special Deals</div>
  <div class="deal-img" role="img" aria-label="Contemporary home with timber deck"></div>
  <div class="deal-text">Description:<br>Lorem Ipsum is simply dummy text of the printing<br>and typesetting industry.<br>Total Area: 400 Sq Yrd.<br>Bedrooms: 3<br>Bathrooms: 4</div>
  <div class="more" style="left:200px;top:272px">More</div>
</section>

<section class="panel" style="left:235px;top:2946px;width:466px;height:183px">
  <div class="panel-head" style="height:42px">Marketing Message</div>
  <p class="msg-text">Lorem Ipsum is simply dummy text of the printing and typesetting industry. Lorem Ipsum has been the industry's standard dummy text ever since the 1500s, when an unknown printer took a galley of type and scrambled it to make a type specimen book. It has survived not only five centuries, but also the leap into electronic typesetting, remaining essentially unchanged. It was popularised in the 1960s with the release of Verrant sheets containing Lorem Ipsum passages, and more recently with desktop publishing software like Quillset Layout including versions of Lorem Ipsum.</p>
</section>

<section class="contact-info">
  <h3>CONTACT INFORMATION</h3>
  <p style="margin-top:14px">Ph: 6378 9152<br>Fax: 6378 9160<br>e-mail:<br>info@tidewellhomes.com.au</p>
</section>

<footer class="footer" style="top:3233px;height:143px"></footer>
<div class="links" style="left:166px;top:3246px"><h4>Links 1</h4><ul><li>Navgation 1</li><li>Navgation 2</li><li>Navgation 3</li><li>Navgation 4</li></ul></div>
<div class="links" style="left:277px;top:3246px"><h4>Links 2</h4><ul><li>Navgation 1</li><li>Navgation 2</li><li>Navgation 3</li><li>Navgation 4</li></ul></div>
<div class="links" style="left:395px;top:3246px"><h4>Links 3</h4><ul><li>Navgation 1</li><li>Navgation 2</li><li>Navgation 3</li><li>Navgation 4</li></ul></div>
<div class="links" style="left:505px;top:3246px"><h4>Links 4</h4><ul><li>Navgation 1</li><li>Navgation 2</li><li>Navgation 3</li><li>Navgation 4</li></ul></div>
<div class="partners" style="top:3250px"><p>Our Parners</p><div class="badge-a"></div><div class="badge-b"></div></div>
<div class="footer-base" style="top:3376px;height:40px">© Tidewell Homes Constructions 2004 Owned and operated by Harrowfield ( Canberra ) Pty Limited<br>ACN 061 372 908 NSW License No. 483052K ACT License No. 3142</div>

</body>
</html>
```